Business Card Design (NEW FILES)

ATTENTION: New vector files are available. Please update your design to reflect/use the new (better resolution) logo images.

Seeking a unique and professional business card design for a commercial drone photography/videography business. The layout should feature
the logo (attached) and include the following information:
978-512-6037
www.skyvantmedia.com
ORD Certified Remote Pilot

```html
<!DOCTYPE html>
<html lang="en">
<head>
<meta charset="utf-8">
<title>Skyvant Media — Business Card</title>
<link rel="stylesheet" href="https://fonts.googleapis.com/css2?family=Poppins:wght@400;500&display=swap">
<style>
  :root {
    --backdrop: #ababab;
    --navy: #131946;
    --orange: #ee8a52;
    --white: #ffffff;
    --ink: #1b1d33;
  }
  * { margin: 0; padding: 0; box-sizing: border-box; }
  html, body {
    width: 1093px;
    height: 1200px;
    overflow: hidden;
    background: var(--backdrop);
    font-family: "Poppins", sans-serif;
  }
  .card {
    position: absolute;
    left: 265px;
    width: 580px;
    height: 356px;
    border-radius: 26px;
    overflow: hidden;
  }
  .card--front { top: 226px; background: var(--white); }
  .card--back  { top: 621px; background: var(--navy); }

  .brand-mark {
    position: absolute;
    left: 384px;
    top: 179px;
    width: 178px;
    height: 178px;
    border-radius: 50%;
    background: var(--navy);
  }
  .holder {
    position: absolute;
    left: 41px;
    top: 190px;
  }
  .holder__name {
    font-weight: 500;
    font-size: 24px;
    line-height: 1.1;
    color: var(--navy);
    letter-spacing: 0.2px;
  }
  .holder__role {
    font-size: 15px;
    line-height: 1.1;
    color: var(--orange);
  }
  .contact {
    position: absolute;
    left: 41px;
    top: 257px;
    list-style: none;
  }
  .contact__item {
    display: flex;
    align-items: center;
    gap: 9px;
    font-size: 16.5px;
    line-height: 21px;
    color: var(--ink);
  }
  .contact__item svg { width: 15px; height: 15px; flex: none; }

  .brand {
    position: absolute;
    left: 0;
    right: 0;
    top: 140px;
    text-align: center;
  }
  .brand__name {
    font-weight: 400;
    font-size: 40px;
    line-height: 1;
    letter-spacing: 1px;
    color: var(--white);
  }
  .brand__tagline {
    margin-top: 10px;
    font-size: 15px;
    letter-spacing: 2px;
    color: var(--orange);
  }
  .credentials {
    position: absolute;
    left: 0;
    right: 0;
    top: 291px;
    text-align: center;
    font-size: 16.5px;
    line-height: 21px;
  }
  .credentials__cert { color: var(--white); }
  .credentials__insured { color: var(--orange); }
</style>
</head>
<body>
  <section class="card card--front">
    <div class="brand-mark" aria-hidden="true"></div>
    <div class="holder">
      <p class="holder__name">MARK DOYLE</p>
      <p class="holder__role">OWNER</p>
    </div>
    <ul class="contact">
      <li class="contact__item">
        <svg viewBox="0 0 24 24" fill="none" stroke="#131946" stroke-width="2.4" stroke-linecap="round" stroke-linejoin="round"><path d="M5 3h4l2 5-2.5 1.5a11 11 0 0 0 6 6L16 13l5 2v4a2 2 0 0 1-2 2A16 16 0 0 1 3 5a2 2 0 0 1 2-2z"/></svg>
        978-512-6037
      </li>
      <li class="contact__item">
        <svg viewBox="0 0 24 24" fill="none" stroke="#131946" stroke-width="2.2"><circle cx="12" cy="12" r="10"/><ellipse cx="12" cy="12" rx="4.5" ry="10"/><path d="M2 12h20M4 7h16M4 17h16"/></svg>
        www.skyvantmedia.com
      </li>
    </ul>
  </section>

  <section class="card card--back">
    <div class="brand">
      <p class="brand__name">SKYVANT MEDIA</p>
      <p class="brand__tagline">CAPTIVATING AERIAL IMAGERY</p>
    </div>
    <div class="credentials">
      <p class="credentials__cert">ORD Certified Remote Pilot</p>
      <p class="credentials__insured">Fully Insured</p>
    </div>
  </section>
</body>
</html>
```